Web Design Project

Revamp current website adding newly designed logo and creating layout that is good on desktops, tablets, and cell phones.

Current website can be viewed at www.venkirainteriors.com

Will you see the website is small but graphics heavy in the gallery. The gallery needs to be setup so that it is easy to maintain the links and update the photos.

Needs to have high visual impact.

I need a new logo and website layout designed for my partner's business. This is a birthday present. His business is interior painting, wallpapering and design. He also has access to a wide variety of products including carpet, fabrics, furniture, wallpaper, tile, countertops, etc. I have attached some screen shots of his website for reference. He is a one man shop and has a stellar reputation with his customers. He is on-time, very tidy, excellent with animals, and always finishes on time and on budget. There are no restrictions on colors or fonts. The logo needs to work well with the website, business cards and printed materials. The website needs to flow content for device size so it looks just as good on a cell phone or tablet as it does on a desktop computer. Whatever the heck that's called! Thanks. I am looking forward to seeing everyone's ideas.

Target Market(s)

Consumers looking for interior design, painting, and wallpapering as well as interior products such as flooring, window treatments, reupholstering, counter tops, etc.

Industry/Entity Type

Cell Phone

Requirements
Must have
• Clean, sharp, visual impact (at least on the home page)
Should not have
• Clutter.

```html
<!DOCTYPE html>
<html lang="en">
<head>
<meta charset="utf-8">
<title>Venkira Interiors</title>
<link href="https://fonts.googleapis.com/css2?family=Cinzel:wght@400;700&family=Open+Sans:ital,wght@0,400;0,600;0,700;1,400&display=swap" rel="stylesheet">
<style>
:root{
  --maroon:#8c1c22;
  --orange:#f7941d;
  --ink:#222;
  --text:#555;
  --rule:#d9d9d9;
  --grey-band:#ececec;
  --footer:#231541;
  --footer-bar:#1a0f30;
  --white:#fff;
}
*{margin:0;padding:0;box-sizing:border-box}
html,body{width:674px;height:1200px;overflow:hidden;background:var(--white)}
body{position:relative;font-family:"Open Sans",Arial,sans-serif;color:var(--text)}
.abs{position:absolute}

/* header */
.topbar{left:0;top:0;width:674px;height:52px;background:var(--maroon)}
.nav{right:28px;top:0;height:52px;display:flex;align-items:center;gap:28px;list-style:none}
.nav li{color:var(--white);font-size:10px;letter-spacing:.3px;text-transform:uppercase}
.nav .has-menu::after{content:"";display:inline-block;width:4px;height:4px;border-right:1px solid #fff;border-bottom:1px solid #fff;transform:rotate(45deg);margin:0 0 3px 6px}
.brand{left:78px;top:8px;width:82px;height:86px;background:var(--white);box-shadow:0 2px 6px rgba(0,0,0,.25);display:flex;flex-direction:column;align-items:center;justify-content:center;gap:6px}
.brand-mark{width:24px;height:24px;background:var(--maroon)}
.brand-name{font-family:"Cinzel",serif;font-weight:700;font-size:11px;line-height:1.15;color:var(--maroon);text-align:center}

/* hero */
.hero{left:0;top:52px;width:674px;height:271px;background:linear-gradient(180deg,#6e5a55 0%,#9a8880 45%,#d8d2cc 75%,#c2b3a3 100%)}
.hero-caption{left:0;top:243px;width:674px;text-align:center;color:var(--white);font-weight:700;font-size:18px;letter-spacing:.3px;text-shadow:0 1px 4px rgba(0,0,0,.8)}

/* section titles */
.section-title{font-family:"Cinzel",serif;font-weight:400;font-size:15px;line-height:20px;color:var(--ink);letter-spacing:.6px}
.section-title .big{font-size:19px}
.rule{height:1px;background:var(--rule)}

/* welcome */
.welcome-title{left:75px;top:345px}
.welcome-rule{left:75px;top:370px;width:524px}
.welcome-photo{left:75px;top:382px;width:113px;height:108px;background:linear-gradient(135deg,#9a8c80,#c23a2b 60%,#7e2a22)}
.welcome-photo-caption{left:75px;top:470px;width:113px;height:20px;background:#2a2a2a;color:var(--white);font-size:8.5px;font-weight:600;display:flex;align-items:center;justify-content:center}
.welcome-text{left:198px;top:382px;width:402px;font-size:7.6px;line-height:1.45}
.welcome-text .lead{color:var(--ink);font-weight:700;margin-bottom:6px}
.btn{background:var(--maroon);color:var(--white);font-size:8px;text-transform:uppercase;display:flex;align-items:center;justify-content:center}
.read-more{left:198px;top:470px;width:60px;height:19px}

/* services */
.services{left:0;top:518px;width:674px;height:172px;background:linear-gradient(180deg,#1f2420 0%,#2f3a30 40%,#4a4a46 70%,#2a2a28 100%)}
.services-title{left:0;top:527px;width:674px;text-align:center;color:var(--white)}
.services-rule{left:270px;top:555px;width:134px;background:rgba(255,255,255,.4)}
.service{top:576px;width:120px;text-align:center;color:var(--white);font-size:10px;font-weight:600;white-space:nowrap}
.service svg{display:block;margin:0 auto 6px}

/* gallery */
.gallery-title{left:0;top:712px;width:674px;text-align:center}
.gallery-rule{left:75px;top:737px;width:524px}
.tile{top:754px;width:120px;height:97px}
.tile-photo{position:absolute;left:0;top:0;width:120px;height:76px}
.tile-caption{position:absolute;left:0;top:76px;width:120px;height:21px;background:var(--maroon);color:var(--white);font-size:8.5px;font-weight:600;display:flex;align-items:center;justify-content:center}

/* review */
.review{left:0;top:882px;width:674px;height:168px;background:var(--grey-band)}
.review-title{left:0;top:891px;width:674px;text-align:center}
.review-rule{left:75px;top:915px;width:524px;background:#cfcfcf}
.avatar{left:313px;top:928px;width:50px;height:50px;border-radius:50%;background:radial-gradient(circle at 50% 40%,#d8c8bc,#3b3f4a 70%);border:2px solid var(--white)}
.arrow{top:958px}
.quote{left:0;top:988px;width:674px;text-align:center;font-style:italic;font-size:11px;color:#333}
.review-text{left:90px;top:1006px;width:494px;text-align:center;font-size:7.4px;line-height:1.45}

/* footer */
.footer{left:0;top:1050px;width:674px;height:128px;background:var(--footer)}
.footer-heading{top:1060px;color:var(--white);font-size:9.5px;font-weight:600;letter-spacing:.6px;text-transform:uppercase}
.quick-links{left:75px;top:1084px;list-style:none;color:var(--white);font-size:8px;line-height:1.95}
.quick-links li::before{content:"›";margin:0 8px 0 4px}
.newsletter-note{left:190px;top:1084px;width:140px;color:var(--white);font-size:8px;line-height:1.45}
.email-field{left:190px;top:1112px;width:138px;height:20px;background:var(--white);color:#777;font-size:8px;display:flex;align-items:center;padding-left:8px;border-radius:2px}
.email-field::before{content:"";width:7px;height:5px;border:1px solid #888;margin-right:6px}
.subscribe{left:190px;top:1138px;width:54px;height:18px;background:#d9d9d9;color:#333;font-size:7.5px;font-weight:600;text-transform:uppercase;display:flex;align-items:center;justify-content:center;border-radius:2px}
.contact{left:369px;top:1082px;color:var(--white);font-size:8px;line-height:1.45}
.contact strong{font-weight:700}
.contact-row{display:flex;align-items:center;gap:7px;margin-top:5px}
.social{left:518px;top:1084px;list-style:none;color:var(--white);font-size:8px}
.social li{display:flex;align-items:center;gap:7px;height:19px}
.social li::before{content:"";width:12px;height:12px;background:var(--white);border-radius:1px}
.footer-bar{left:0;top:1178px;width:674px;height:22px;background:var(--footer-bar)}
.copyright{left:75px;top:1185px;color:#ddd;font-size:7.5px}
.legal{right:75px;top:1185px;color:#ddd;font-size:7.5px;display:flex;gap:8px}
</style>
</head>
<body>

<!-- header -->
<div class="abs topbar"></div>
<ul class="abs nav">
  <li>Home</li><li>About</li><li>Contact</li><li class="has-menu">Gallery</li><li>Products</li><li>Services</li>
</ul>
<div class="abs hero" role="img" aria-label="Photo of a modern living room with a white sofa, cushions and framed wall art"></div>
<div class="abs hero-caption">Lorem Ipsum Dolor Amet Consectetur</div>
<div class="abs brand">
  <div class="brand-mark"></div>
  <div class="brand-name">VENKIRA<br>INTERIORS</div>
</div>

<!-- welcome -->
<h1 class="abs section-title welcome-title"><span class="big">W</span>ELCOME <span class="big">T</span>O <span class="big">V</span>ENKIRA <span class="big">I</span>NTERIORS</h1>
<div class="abs rule welcome-rule"></div>
<div class="abs welcome-photo" role="img" aria-label="Photo of a red sofa beside a potted plant"></div>
<div class="abs welcome-photo-caption">Lorem Lisum Simply</div>
<div class="abs welcome-text">
  <p class="lead">Lorem ipsum dolor sit amet, consectetur adipisicing elit, sed do eiusmod tem incididunt ut labore ieho et dolore magna aliqua. Ut enim ad minim veniam.</p>
  <p>Duis aute irure dolor in reprehenderinim voluptate velit esse cillum dolore eu fugiat nulla pariatur Excepteur sint occaecat cupidatat non proident, sunt in culpa qui officia deserunt mollit anim id est laborum Neque porro quisquam est, q dolorem ipsum quo consectetur suscipit laboriosam nisi ut aliquid ex ea commodi consequatur Duis aute irure dolor reprehenderit in voluptate velit esse cillum dolore eu fugiat nulla pariatur. Excepteur sint occaecat cupidatat non proidn, sunt in culpa qui officia deserunt mollit anim id est laborum</p>
</div>
<div class="abs btn read-more">Read More</div>

<!-- services -->
<div class="abs services" role="img" aria-label="Dim photo of an outdoor lounge with sofas and garden trees"></div>
<h2 class="abs section-title services-title"><span class="big">O</span>UR <span class="big">S</span>ERVICES</h2>
<div class="abs rule services-rule"></div>

<div class="abs service" style="left:66px">
  <svg width="64" height="72" viewBox="0 0 64 72"><polygon points="32,0 64,18 64,54 32,72 0,54 0,18" fill="#f7941d"/><g fill="#fff"><rect x="18" y="40" width="28" height="6"/><rect x="20" y="46" width="3" height="6"/><rect x="41" y="46" width="3" height="6"/><rect x="18" y="24" width="8" height="14"/><rect x="30" y="30" width="16" height="8"/></g></svg>
  Interior Design
</div>
<div class="abs service" style="left:172px">
  <svg width="64" height="72" viewBox="0 0 64 72"><polygon points="32,0 64,18 64,54 32,72 0,54 0,18" fill="#f7941d"/><ellipse cx="30" cy="38" rx="15" ry="12" fill="#fff"/><g fill="#f7941d"><circle cx="24" cy="33" r="2.5"/><circle cx="31" cy="31" r="2.5"/><circle cx="37" cy="36" r="2.5"/><circle cx="27" cy="43" r="3"/></g><rect x="38" y="18" width="4" height="22" fill="#fff" transform="rotate(35 40 29)"/></svg>
  Painting
</div>
<div class="abs service" style="left:276px">
  <svg width="64" height="72" viewBox="0 0 64 72"><polygon points="32,0 64,18 64,54 32,72 0,54 0,18" fill="#f7941d"/><g fill="#fff"><rect x="16" y="24" width="14" height="6"/><rect x="32" y="24" width="16" height="6"/><rect x="16" y="32" width="8" height="6"/><rect x="26" y="32" width="14" height="6"/><rect x="42" y="32" width="6" height="6"/><rect x="16" y="40" width="14" height="6"/><rect x="32" y="40" width="16" height="6"/></g></svg>
  Wallpapering
</div>
<div class="abs service" style="left:382px">
  <svg width="64" height="72" viewBox="0 0 64 72"><polygon points="32,0 64,18 64,54 32,72 0,54 0,18" fill="#f7941d"/><g fill="#fff" transform="rotate(45 32 36)"><rect x="21" y="25" width="10" height="10"/><rect x="33" y="25" width="10" height="10"/><rect x="21" y="37" width="10" height="10"/><rect x="33" y="37" width="10" height="10"/></g></svg>
  Flooring
</div>
<div class="abs service" style="left:486px">
  <svg width="64" height="72" viewBox="0 0 64 72"><polygon points="32,0 64,18 64,54 32,72 0,54 0,18" fill="#f7941d"/><path d="M20 52V32a12 12 0 0 1 24 0v20z" fill="#fff"/><g stroke="#f7941d" stroke-width="2"><line x1="32" y1="22" x2="32" y2="52"/><line x1="20" y1="36" x2="44" y2="36"/></g></svg>
  Window Treatments
</div>

<!-- gallery -->
<h2 class="abs section-title gallery-title"><span class="big">O</span>UR <span class="big">G</span>ALLERY</h2>
<div class="abs rule gallery-rule"></div>
<div class="abs tile" style="left:75px"><div class="tile-photo" role="img" aria-label="Photo of a bright orange living room with a wall unit" style="background:linear-gradient(135deg,#e2621c,#f0c020 70%,#c84a18)"></div><div class="tile-caption">Lorem ipsum dolor</div></div>
<div class="abs tile" style="left:208px"><div class="tile-photo" role="img" aria-label="Photo of a modern white and grey kitchen" style="background:linear-gradient(135deg,#d9d6d0,#8f8a84 60%,#c8c4bf)"></div><div class="tile-caption">Lorem ipsum dolor</div></div>
<div class="abs tile" style="left:343px"><div class="tile-photo" role="img" aria-label="Photo of a paint roller on a purple wall" style="background:linear-gradient(135deg,#6a4a8a,#b6a3c8 60%,#e9e2ee)"></div><div class="tile-caption">Lorem ipsum dolor</div></div>
<div class="abs tile" style="left:477px"><div class="tile-photo" role="img" aria-label="Photo of a grey living room with a mounted television" style="background:linear-gradient(135deg,#e8e8e8,#9a9a9a 55%,#3a3a3a)"></div><div class="tile-caption">Lorem ipsum dolor</div></div>

<!-- review -->
<div class="abs review"></div>
<h2 class="abs section-title review-title"><span class="big">O</span>UR <span class="big">C</span>USTOMER <span class="big">R</span>EVIEW</h2>
<div class="abs rule review-rule"></div>
<div class="abs avatar" role="img" aria-label="Portrait photo of a customer"></div>
<svg class="abs arrow" style="left:74px" width="10" height="18" viewBox="0 0 10 18"><polyline points="9,1 1,9 9,17" fill="none" stroke="#bbb" stroke-width="2"/></svg>
<svg class="abs arrow" style="left:590px" width="10" height="18" viewBox="0 0 10 18"><polyline points="1,1 9,9 1,17" fill="none" stroke="#bbb" stroke-width="2"/></svg>
<p class="abs quote">Vestibulum porta, diam quis auctor ultricies, dui quam dapibus ligula, consectetur</p>
<p class="abs review-text">Lorem ipsum dolor sit amet, consectetur adipiscing elit. Integer venenatis tincidunt elit, aliquam semper quam pulvinar id. Aliquam erat volutpat. Integer nulla urna, sagittis sed viverra quis, tincidunt vel felis. Pellentesque eleifend sem ut diam bibendum, non sagittis sapien pellentesque. Etiam semper</p>

<!-- footer -->
<div class="abs footer"></div>
<h3 class="abs footer-heading" style="left:75px">Quick Links</h3>
<ul class="abs quick-links"><li>Home</li><li>About</li><li>Gallery</li><li>Products</li><li>Services</li></ul>

<h3 class="abs footer-heading" style="left:190px">Newsletter Sign Up</h3>
<p class="abs newsletter-note">Stay Updated With Latest News From Venkira Interiors</p>
<div class="abs email-field">Enter your Email</div>
<div class="abs subscribe">Subscribe</div>

<h3 class="abs footer-heading" style="left:369px">Contact Information</h3>
<div class="abs contact">
  <strong>Venkira Interiors</strong><br>
  123 Lorem ipsum dolor Eros,<br>WA 0000,
  <div class="contact-row"><svg width="9" height="9" viewBox="0 0 10 10"><path d="M2 0h2l1 3-1.5 1a6 6 0 0 0 2.5 2.5L7 5l3 1v2c0 1-1 2-2 2A8 8 0 0 1 0 2c0-1 1-2 2-2z" fill="#fff"/></svg>123-456-7890</div>
  <div class="contact-row"><svg width="9" height="9" viewBox="0 0 10 10"><rect x="2" y="0" width="6" height="3" fill="#fff"/><rect x="0" y="3" width="10" height="5" fill="#fff"/><rect x="2" y="6" width="6" height="4" fill="#fff" stroke="#231541"/></svg>123-456-7890</div>
  <div class="contact-row"><svg width="9" height="9" viewBox="0 0 10 10"><circle cx="5" cy="5" r="4" fill="none" stroke="#fff" stroke-width="1.5"/><circle cx="5" cy="5" r="1.5" fill="#fff"/></svg>info@venkirainteriors.com</div>
</div>

<h3 class="abs footer-heading" style="left:518px">Follow Us</h3>
<ul class="abs social"><li>Friendloop</li><li>Chirpline</li><li>Circlebook</li><li>Workmesh</li></ul>

<div class="abs footer-bar"></div>
<p class="abs copyright">© 2014 Venkira Interiors &nbsp;|&nbsp; All Rights Reserved</p>
<p class="abs legal"><span>Faq's</span><span>|</span><span>Contact</span><span>|</span><span>Privacy Policy</span></p>

</body>
</html>
```